Paraffin Wax Packaging Design for Nail and Beauty Industry

We need an attractive design for the packaging of our new product, Paraffin Wax. Our company is a wholesale beauty/nail supply company that has been selling to nail salons in the US market for 10 years. We currently sell this product that we buy from another company. Now we want to launch our own brand of Paraffin Wax.

Target Market(s)

Retail nail salons in the US market.

Industry/Entity Type

Industry

Font styles to use
Sans Serif

Colors

Designer to choose colors to be used in the design.

Requirements
Must have
• Our logo (attached).
• All information on the "Ingredient List" (attached).
• Design for Clear Packaging so product can show through.
• Design for Package Dimensions of 4.25" x 11" (110cm x 280 cm).
Nice to have
• Picture related to women's skin and or beauty.
• Contrast as in the design of product that we currently sell (attached).

```html
<!DOCTYPE html>
<html lang="en">
<head>
<meta charset="UTF-8">
<title>By Corvella Antibacterial Paraffin Wax – Package Front</title>
<link href="https://fonts.googleapis.com/css2?family=Montserrat:wght@500&family=Oswald:wght@300;400;500&display=swap" rel="stylesheet">
<style>
  :root {
    --pink: #f088b8;
    --periwinkle: #6b85c4;
    --navy: #463f8a;
    --white: #ffffff;
    --ink: #2a2a2a;
    --page: #ffffff;
    --edge: #c9c9c9;
  }
  * { margin: 0; padding: 0; box-sizing: border-box; }
  html, body { width: 1200px; height: 1200px; overflow: hidden; background: var(--page); }
  .stage { position: relative; width: 1200px; height: 1200px; }
  .package-front {
    position: absolute; left: 408px; top: 120px;
    width: 480px; height: 1200px;
    transform: scale(0.8); transform-origin: top left;
    background: var(--white);
    outline: 1px solid var(--edge);
    overflow: hidden;
  }
  .shapes { position: absolute; inset: 0; }
  .brand-name {
    position: absolute; top: 130px; left: 0; width: 480px;
    text-align: center;
    font-family: "Montserrat", sans-serif; font-weight: 500;
    font-size: 44px; color: var(--ink); letter-spacing: 1px;
  }
  .title-antibacterial {
    position: absolute; left: 40px; top: 283px;
    font-family: "Montserrat", sans-serif; font-weight: 500;
    font-size: 46px; color: var(--white); line-height: 60px;
  }
  .title-paraffin {
    position: absolute; right: 30px; top: 357px;
    font-family: "Montserrat", sans-serif; font-weight: 500;
    font-size: 46px; color: var(--white); line-height: 60px;
  }
  .claims { position: absolute; left: 45px; top: 462px; color: var(--white); font-family: "Oswald", sans-serif; }
  .claims .compatible { font-weight: 400; font-size: 24px; line-height: 30px; }
  .claims .moisturize { font-weight: 300; font-size: 24px; line-height: 30px; margin-top: 14px; opacity: 0.92; }
  .product-photo { position: absolute; left: 0; top: 637px; width: 330px; height: 488px; }
  .info {
    position: absolute; right: 30px; width: 260px; text-align: right;
    font-family: "Oswald", sans-serif; color: var(--ink);
  }
  .info h3 { font-weight: 500; font-size: 15px; line-height: 25px; }
  .info p { font-weight: 300; font-size: 14px; line-height: 25px; }
  .info-ingredients { top: 685px; }
  .info-caution { top: 811px; }
  .net-weight {
    position: absolute; right: 0; top: 947px; width: 128px; height: 93px;
    background: var(--navy); border-radius: 14px 0 0 32px;
    padding: 12px 30px 0 0; text-align: right;
    font-family: "Montserrat", sans-serif; font-weight: 500;
    font-size: 16px; line-height: 21px; color: var(--white);
  }
</style>
</head>
<body>
<div class="stage">
  <div class="package-front">
    <svg class="shapes" width="480" height="1200" viewBox="0 0 480 1200" aria-hidden="true">
      <path class="tab-top" fill="var(--pink)" d="M30 0 H450 C430 10 420 30 410 50 C400 68 390 75 370 75 H110 C90 75 80 68 70 50 C60 30 50 10 30 0 Z"/>
      <path class="band-antibacterial" fill="var(--periwinkle)" d="M0 277 H348 Q368 277 368 297 V350 H0 Z"/>
      <path class="block-pink" fill="var(--pink)" d="M0 350 H480 V560 C440 565 425 600 410 620 C400 632 390 637 375 637 H0 Z"/>
      <path class="band-paraffin" fill="var(--navy)" d="M55 350 H480 V425 H130 C100 425 95 395 80 375 C72 362 65 352 55 350 Z"/>
      <path class="tab-bottom" fill="var(--navy)" d="M30 1200 H450 C430 1190 420 1170 410 1150 C400 1132 390 1125 370 1125 H110 C90 1125 80 1132 70 1150 C60 1170 50 1190 30 1200 Z"/>
    </svg>

    <div class="brand-name">By Corvella</div>

    <div class="title-antibacterial">antibacterial</div>
    <div class="title-paraffin">paraffin wax</div>

    <div class="claims">
      <div class="compatible">COMPATIBLE FOR USE WITH MOST<br>WAX PARAFFIN HEAT THERAPY UNITS</div>
      <div class="moisturize">DEEPLY MOISTURIZES THE SKIN RESTORING<br>A HEALTHIER LOOK AND FEEL TO SKIN.</div>
    </div>

    <svg class="product-photo" viewBox="0 0 330 488" role="img" aria-label="Photo of a woman in a white towel seated, touching her smooth legs">
      <defs>
        <radialGradient id="skinTone" cx="45%" cy="55%" r="70%">
          <stop offset="0%" stop-color="#efd2bf"/>
          <stop offset="60%" stop-color="#f5e4d8"/>
          <stop offset="100%" stop-color="#ffffff"/>
        </radialGradient>
      </defs>
      <rect width="330" height="488" fill="url(#skinTone)"/>
    </svg>

    <div class="info info-ingredients">
      <h3>Ingredients:</h3>
      <p>Paraffin waxes and Hydrocarbon waxes,<br>Petrolatum, Paraffin oils, Apricot<br>kernel oil, Fragrance D &amp; C dyes.</p>
    </div>
    <div class="info info-caution">
      <h3>Caution:</h3>
      <p>Paraffin is flammable. Do not use near<br>open flame or an unprotected<br>resistance heater.</p>
    </div>

    <div class="net-weight">Net Wt.<br>1 lb.<br>(450 g.)</div>
  </div>
</div>
</body>
</html>
```